Professional Learning Organization for Educators needs a Design Thinking Workshop Flyer

We need a flyer for a series of Introductory Design Thinking workshops we're delivering for education leaders.

We have generated our own version of the flyer with a word template, but want it to look even more professional and eye catching. It is attached.

We had an image that we thought might be good, but pulled it out so we don't bias designers' thinking.
Updates

Reason: We are a bit flexible on the deadline since this is a holiday week and people are traveling

Target Market(s)

Very busy education leaders whose curiosity needs to be stimulated enough to enroll in the course

Industry/Entity Type

Education

Font styles to use
Other font styles liked:
• Century Gothic or something closer to that

Requirements
Must have
• Some version of the text that is on the current flyer that I attached.
Nice to have
• I am very flexible and open right now on this design.

```html
<!DOCTYPE html>
<html lang="en">
<head>
<meta charset="utf-8">
<title>Design Thinking Workshops</title>
<link href="https://fonts.googleapis.com/css2?family=Cabin+Condensed:wght@500;600;700&family=Arimo:wght@400&display=swap" rel="stylesheet">
<style>
  :root {
    --page-bg: #e6e7e9;
    --board-dark: #4f5f70;
    --board-mid: #627487;
    --board-light: #75879a;
    --title-yellow: #f2e31c;
    --subtitle-grey: #e9ecef;
    --quote-panel-top: #c3def1;
    --quote-panel-bottom: #d6e9f6;
    --info-panel-top: #e2e5e9;
    --info-panel-bottom: #eef0f2;
    --heading-cyan: #1ba2dd;
    --divider-grey: #979a9e;
    --ink: #1f2327;
    --body-ink: #2b2f33;
  }
  * { margin: 0; padding: 0; box-sizing: border-box; }
  html, body { width: 1200px; height: 1200px; overflow: hidden; }
  body { background: var(--page-bg); position: relative; }

  .flyer {
    position: absolute;
    left: 208px; top: 30px;
    width: 783px; height: 1140px;
    background: #fff;
    box-shadow: 0 2px 10px rgba(0,0,0,0.12);
    overflow: hidden;
  }

  .hero {
    position: absolute; left: 0; top: 0;
    width: 783px; height: 520px;
  }
  .hero-photo {
    position: absolute; inset: 0;
    background:
      radial-gradient(ellipse 260px 420px at 175px 330px, rgba(200,205,210,0.55), rgba(200,205,210,0) 70%),
      linear-gradient(160deg, var(--board-light) 0%, var(--board-mid) 45%, var(--board-dark) 100%);
  }
  .hero-title {
    position: absolute; left: 329px; top: 72px;
    font-family: "Cabin Condensed", sans-serif;
    font-weight: 700;
    font-size: 72px;
    line-height: 90px;
    color: var(--title-yellow);
    letter-spacing: 1px;
  }
  .hero-tagline {
    position: absolute; right: 12px; top: 368px;
    text-align: right;
    font-family: "Cabin Condensed", sans-serif;
    font-weight: 600;
    font-size: 38px;
    line-height: 51px;
    color: var(--subtitle-grey);
    letter-spacing: 1px;
  }

  .testimonials {
    position: absolute; left: 0; top: 520px;
    width: 394px; height: 620px;
    background: linear-gradient(180deg, var(--quote-panel-top), var(--quote-panel-bottom));
  }
  .testimonials-heading {
    margin-top: 14px;
    text-align: center;
    font-family: "Cabin Condensed", sans-serif;
    font-weight: 500;
    font-size: 38px;
    line-height: 46px;
    color: var(--heading-cyan);
    letter-spacing: 1px;
  }
  .quote {
    position: absolute; left: 22px; width: 356px;
    font-family: "Cabin Condensed", sans-serif;
    font-weight: 600;
    font-size: 17.5px;
    line-height: 25px;
    color: var(--ink);
    letter-spacing: 0.3px;
  }
  .quote-one { top: 132px; }
  .quote-two { top: 328px; }
  .quote-three { top: 512px; }
  .quote-divider {
    position: absolute; left: 22px; width: 356px; height: 6px;
    background: var(--divider-grey);
  }
  .divider-one { top: 265px; }
  .divider-two { top: 449px; }

  .course-info {
    position: absolute; left: 394px; top: 520px;
    width: 389px; height: 620px;
    padding: 16px 14px 0 21px;
    background: linear-gradient(160deg, var(--info-panel-top), var(--info-panel-bottom));
    font-family: "Arimo", sans-serif;
    font-size: 15.5px;
    line-height: 27.5px;
    color: var(--body-ink);
  }
  .course-info p { margin-bottom: 14px; }
  .session-list { list-style: none; margin: -14px 0 14px 0; }
  .session-list li { position: relative; padding-left: 24px; }
  .session-list li::before {
    content: ""; position: absolute; left: 4px; top: 12px;
    width: 5px; height: 5px; border-radius: 50%; background: var(--body-ink);
  }
</style>
</head>
<body>
  <main class="flyer">
    <section class="hero">
      <div class="hero-photo" role="img" aria-label="Photo of a smiling teacher holding chalk in front of a slate-blue chalkboard"></div>
      <h1 class="hero-title">Design<br>Thinking<br>Workshops</h1>
      <p class="hero-tagline">Design Your Way to<br>Better Solutions</p>
    </section>

    <section class="testimonials">
      <h2 class="testimonials-heading">WHAT OUR<br>PARTICIPANTS SAY...</h2>
      <blockquote class="quote quote-one">“This has been an empowering experience that allowed me to try out dramatic changes in my practice that I wouldn’t have imagined before.”</blockquote>
      <div class="quote-divider divider-one"></div>
      <blockquote class="quote quote-two">“I never realized how often I’ve guessed and assumed what our teachers and students need – now I have a way to stop guessing!”</blockquote>
      <div class="quote-divider divider-two"></div>
      <blockquote class="quote quote-three">“I finally have tools to generate truly creative ideas that people actually embrace… because they meet their needs”</blockquote>
    </section>

    <section class="course-info">
      <p>Cedar Valley Public Schools and Summit Ridge Learning Cooperative invite you to discover the power of Design Thinking.</p>
      <p>During our three session course, you will learn and practice mindsets and tools that help you continuously and creatively improve the experiences of the people you serve.</p>
      <p>We are offering this three-session course at four different times in spring semester.&nbsp; Please choose the course that works best for your schedule.</p>
      <ul class="session-list">
        <li>Monday mornings: 1/23, 1/30 and 2/6</li>
        <li>Tuesday afternoons: 2/7, 2/14 and 2/21</li>
        <li>Wednesday afternoons: 3/8, 3/15 and 3/22</li>
        <li>Wednesday evenings: 2/8, 2/15 and 2/22</li>
      </ul>
      <p>Go to www.summitridgelearn.org to learn more.</p>
      <p>This course is held in Cedar Valley Public Schools.&nbsp; No fee for CVPS leaders.&nbsp; $150 fee for leaders outside of CVPS.</p>
    </section>
  </main>
</body>
</html>
```